Life Coach for Lawyers Business Card Design

Elegant, original, business card design for life coaching service for associate attorneys who work in big law and struggle with stress, overwhelm, and time management. Double sided design.

Target Market(s)

Women associate attorneys who work in big law and struggle with stress, overwhelm, and time management.

Industry/Entity Type

Life Coaching

Contact Information for Business Card

Marlene Quorthby
Life Coach
519.607.4431
brightcounselpath.net
marlene@brightcounselpath.net
@brightcounselpath (Instagram)

Font styles to use
Other font styles liked:
• Silver South font duo. See uploaded files.

Requirements
Must have
• Icons for phone, website, email, and Instagram instead of words. Specific colors used in my logo (171B2B, 421121, FFFFFF)
Nice to have
• Foil. Embossed. Feminine design.
Should not have
• Any colors other than those used in logo. See uploaded files.

```html
<!DOCTYPE html>
<html lang="en">
<head>
<meta charset="utf-8">
<title>Bright Counsel Path – Business Card</title>
<link href="https://fonts.googleapis.com/css2?family=Libre+Baskerville:wght@400&display=swap" rel="stylesheet">
<style>
  :root {
    --navy: #171B2B;
    --maroon: #421121;
    --white: #FFFFFF;
    --backdrop: #e9e6e7;
    --foil: #b7b1b4;
    --ink-soft: #5a5c66;
  }
  * { box-sizing: border-box; margin: 0; padding: 0; }
  html, body { width: 1200px; height: 864px; overflow: hidden; }
  body {
    background: var(--backdrop);
    font-family: "Libre Baskerville", "Times New Roman", serif;
    position: relative;
  }
  .card {
    position: absolute;
    left: 250px;
    width: 700px;
    height: 400px;
    box-shadow: 0 6px 18px rgba(23, 27, 43, 0.18);
  }
  .card--front { top: 22px; background: var(--maroon); }
  .card--back  { top: 442px; background: var(--white); }

  .front-wordmark {
    position: absolute;
    inset: 0;
    display: flex;
    align-items: center;
    justify-content: center;
    color: var(--foil);
    font-size: 44px;
    letter-spacing: 0.04em;
  }

  .back-layout {
    position: absolute;
    inset: 0;
    display: flex;
    align-items: center;
    padding: 0 0 0 48px;
  }
  .back-wordmark {
    width: 250px;
    flex: none;
    color: var(--maroon);
    font-size: 30px;
    line-height: 1.2;
    letter-spacing: 0.03em;
    text-align: right;
  }
  .divider {
    width: 1px;
    height: 160px;
    flex: none;
    background: var(--navy);
    opacity: 0.55;
    margin: 0 24px 0 26px;
  }
  .contact { color: var(--navy); }
  .contact__name {
    color: var(--maroon);
    font-size: 22px;
    line-height: 1.2;
  }
  .contact__role {
    font-size: 14px;
    margin: 2px 0 12px;
  }
  .contact__row {
    display: flex;
    align-items: center;
    gap: 8px;
    font-size: 14px;
    color: var(--ink-soft);
    line-height: 1.6;
    white-space: nowrap;
  }
  .contact__icon { width: 13px; height: 13px; flex: none; }
</style>
</head>
<body>
  <section class="card card--front" aria-label="Card front">
    <div class="front-wordmark">Bright Counsel Path</div>
  </section>

  <section class="card card--back" aria-label="Card back">
    <div class="back-layout">
      <div class="back-wordmark">Bright Counsel<br>Path</div>
      <div class="divider"></div>
      <div class="contact">
        <p class="contact__name">Marlene Quorthby</p>
        <p class="contact__role">Life Coach</p>
        <p class="contact__row">
          <svg class="contact__icon" viewBox="0 0 16 16" aria-label="Phone">
            <circle cx="8" cy="8" r="7.5" fill="#421121"/>
            <path d="M5.2 4.2 L6.6 4 L7.3 5.9 L6.4 6.6 Q7.2 8.4 9.2 9.6 L10 8.7 L11.9 9.4 L11.7 10.8 Q11 11.8 9.6 11.4 Q5.6 10 4.5 6 Q4.3 4.8 5.2 4.2 Z" fill="#FFFFFF"/>
          </svg>
          519.607.4431
        </p>
        <p class="contact__row">
          <svg class="contact__icon" viewBox="0 0 16 16" aria-label="Email">
            <rect x="1" y="3" width="14" height="10" rx="1.5" fill="#421121"/>
            <path d="M1.5 4 L8 9 L14.5 4" fill="none" stroke="#FFFFFF" stroke-width="1.3"/>
          </svg>
          marlene@brightcounselpath.net
        </p>
        <p class="contact__row">
          <svg class="contact__icon" viewBox="0 0 16 16" aria-label="Website">
            <circle cx="8" cy="8" r="7" fill="#421121"/>
            <ellipse cx="8" cy="8" rx="3" ry="6.2" fill="none" stroke="#FFFFFF" stroke-width="1"/>
            <line x1="1.5" y1="8" x2="14.5" y2="8" stroke="#FFFFFF" stroke-width="1"/>
          </svg>
          brightcounselpath.net
        </p>
        <p class="contact__row">
          <svg class="contact__icon" viewBox="0 0 16 16" aria-label="Social handle">
            <circle cx="8" cy="8" r="7" fill="#421121"/>
          </svg>
          @brightcounselpath
        </p>
      </div>
    </div>
  </section>
</body>
</html>
```